Dietitian/Nutritionist seeks trifold marketing brochure

We need a trifold brochure for marketing to patients within a doctors surgery. This will be a source of information for prospective patients, what they can expect and how to contact us. The brochure needs to have some key information such as a brief description of the services available, fees, locations of clinics and contact information. Our current brochure has been uploaded which has the information you need to complete this project. The files you provide will allow us to edit the information at a later date as pricing and services change.

Target Market(s)

Patients who have been referred to see a dietitian/nutritionist and people who are considering seeing a dietitian/nutritionist but haven't decided

Industry/Entity Type

Dietician

Font styles to use
Serif

Colors

Designer to choose colors to be used in the design.

Requirements
Must have
• My logo
• Verified clinical mealwise logo
• My website address and contact details
• Most of the information that is in my current brochure
• Locations/names of the four clinics
Nice to have
• Images that promote cooking, health and wellbeing

```html
<!DOCTYPE html>
<html lang="en">
<head>
<meta charset="utf-8">
<title>Riverbend Nutrition &amp; Dietetics – Trifold Brochure</title>
<link href="https://fonts.googleapis.com/css2?family=Arimo:wght@400;700&family=Federo&display=swap" rel="stylesheet">
<style>
  :root {
    --page-bg: #eeeae5;
    --paper: #ffffff;
    --ink: #1f1f1f;
    --brand-blue: #1f3f93;
    --brand-blue-light: #2a63b8;
    --brand-green: #7cbf2c;
    --brand-green-dark: #4a9a2a;
    --badge-orange: #f07a24;
  }
  *, *::before, *::after { box-sizing: border-box; }
  html, body {
    margin: 0; padding: 0;
    width: 1200px; height: 1200px;
    overflow: hidden;
    background: var(--page-bg);
  }
  .brochure {
    position: absolute;
    left: 0; top: 135px;
    width: 1300px; height: 1008px;
    transform: scale(0.923);
    transform-origin: 0 0;
    background: var(--paper);
    font-family: "Arimo", Arial, sans-serif;
    color: var(--ink);
  }
  .panel { position: absolute; top: 0; height: 1008px; overflow: hidden; }
  .panel--services { left: 0; width: 430px; }
  .panel--about { left: 430px; width: 430px; }
  .panel--cover { left: 860px; width: 440px; }

  /* Services panel */
  .services__image {
    position: absolute; left: 30px; top: 40px; width: 390px; height: 220px;
    background: radial-gradient(ellipse at 40% 55%, #d8344a 0%, #c02a3e 35%, rgba(120,180,60,.9) 62%, #ffffff 80%);
    border-radius: 50%;
  }
  .services__title {
    position: absolute; left: 40px; top: 292px; width: 375px;
    text-align: center; font-weight: 700; font-size: 21px; line-height: 27px; margin: 0;
  }
  .services__list {
    position: absolute; left: 48px; top: 370px; width: 360px;
    margin: 0; padding: 0 0 0 24px;
    font-size: 21px; line-height: 27.5px;
  }
  .services__list li { margin-bottom: 22px; }
  .web-bar {
    position: absolute; left: 0; bottom: 0; width: 430px; height: 56px;
    background: linear-gradient(90deg, var(--brand-blue) 0%, var(--brand-blue-light) 100%);
    color: #fff; font-family: "Federo", serif; font-size: 21px;
    display: flex; align-items: center; justify-content: center; letter-spacing: .3px;
  }

  /* About panel */
  .about__top, .about__bottom { position: absolute; left: 0; width: 430px; }
  .about__top { top: 0; height: 330px; }
  .about__bottom { top: 690px; height: 318px; }
  .about__text {
    position: absolute; left: 40px; top: 330px; width: 365px;
    text-align: center; font-size: 21px; line-height: 32.5px; margin: 0;
  }
  .about__text p { margin: 0 0 22px; }

  /* Cover panel */
  .brand {
    position: absolute; left: 30px; top: 40px; width: 400px;
    display: flex; align-items: center; gap: 14px;
  }
  .brand__dot { width: 80px; height: 80px; border-radius: 50%; background: var(--brand-blue); flex: none; }
  .brand__name { font-size: 27px; font-weight: 700; color: var(--brand-blue); line-height: 32px; }
  .cover__visual { position: absolute; left: 0; top: 120px; width: 440px; height: 580px; }
  .contact {
    position: absolute; left: 0; top: 670px; width: 440px;
    text-align: center; font-family: "Federo", serif; color: var(--ink);
  }
  .contact__name { font-size: 28px; margin: 0 0 6px; }
  .contact__line { font-size: 17px; margin: 0 0 12px; }
  .contact__fax { font-size: 21px; margin: 36px 0 8px; }
  .contact__web { font-size: 15px; margin: 0 0 10px; }
  .contact__role { font-size: 25px; margin: 0; }
  .badge {
    position: absolute; left: 227px; top: 914px; width: 172px; height: 82px;
    background: var(--badge-orange); border-radius: 4px;
  }
  .badge::after {
    content: ""; position: absolute; right: 16px; top: 9px;
    width: 64px; height: 64px; border-radius: 50%; background: #fff;
  }
</style>
</head>
<body>
<main class="brochure">

  <section class="panel panel--services">
    <div class="services__image" role="img" aria-label="Photo of fresh raspberries with green leaves"></div>
    <h2 class="services__title">A Verified clinical mealwise<br>can assist you with:</h2>
    <ul class="services__list">
      <li>Diabetes – Impaired Glucose Tolerance, Type 1 &amp; 2 Diabetes, Gestational Diabetes</li>
      <li>Digestive Health– Irritable Bowel Syndrome, Coeliac Disease, Diverticular Disease</li>
      <li>Gastric banding and other surgical methods of weight loss</li>
      <li>Cardiovascular - High cholesterol, High Blood Pressure, Risk Reduction</li>
      <li>Weight Management – loss/gain and support</li>
      <li>General Healthy Eating &amp; Nutrition</li>
    </ul>
    <div class="web-bar">www.riverbenddietitian.example</div>
  </section>

  <section class="panel panel--about">
    <svg class="about__top" viewBox="0 0 430 330">
      <defs>
        <linearGradient id="fruitTones" x1="0" y1="0" x2="1" y2="1">
          <stop offset="0" stop-color="#f9b233"/>
          <stop offset="0.5" stop-color="#f28a1e"/>
          <stop offset="1" stop-color="#9bb83a"/>
        </linearGradient>
        <linearGradient id="swooshA" x1="0" x2="1">
          <stop offset="0" stop-color="#7cbf2c"/><stop offset="1" stop-color="#2a63b8"/>
        </linearGradient>
      </defs>
      <path role="img" aria-label="Photo of citrus fruit, kiwifruit, juice and a stethoscope" d="M0 0H430V300C330 260 120 255 0 275Z" fill="url(#fruitTones)"/>
      <path d="M0 268C120 248 330 252 430 296V306C330 268 120 268 0 290Z" fill="url(#swooshA)"/>
      <path d="M0 290C120 268 330 268 430 306V330H0Z" fill="#ffffff"/>
      <path d="M0 292C110 262 300 262 430 306L430 300C310 258 110 252 0 280Z" fill="#1f3f93"/>
    </svg>
    <div class="about__text">
      <p>Helping you to meet your individual nutrition goals with an emphasis on practical skills, everyday foods, and providing you</p>
      <p>with up to date advice.</p>
      <p>We work together to develop personalised eating plans that take into consideration your food preferences, health, work, family and lifestyle needs.</p>
    </div>
    <svg class="about__bottom" viewBox="0 0 430 318">
      <defs>
        <linearGradient id="swooshB" x1="0" x2="1">
          <stop offset="0" stop-color="#1f3f93"/><stop offset="1" stop-color="#7cbf2c"/>
        </linearGradient>
        <radialGradient id="garlicTones" cx="0.5" cy="0.55" r="0.5">
          <stop offset="0" stop-color="#f3ece0"/><stop offset="0.6" stop-color="#e2d6c4"/><stop offset="1" stop-color="#ffffff"/>
        </radialGradient>
      </defs>
      <path d="M0 18C120 60 320 60 430 0V12C320 60 120 70 0 28Z" fill="#1f3f93"/>
      <path d="M60 40C180 70 340 56 430 10V40C330 70 190 70 60 40Z" fill="url(#swooshB)"/>
      <rect role="img" aria-label="Photo of garlic bulbs and cloves with parsley" x="40" y="80" width="360" height="230" rx="110" fill="url(#garlicTones)"/>
    </svg>
  </section>

  <section class="panel panel--cover">
    <div class="brand">
      <span class="brand__dot"></span>
      <span class="brand__name">Riverbend<br>Nutrition &amp; Dietetics</span>
    </div>
    <svg class="cover__visual" viewBox="0 0 440 580">
      <defs>
        <linearGradient id="kitchenTones" x1="0" y1="0" x2="1" y2="1">
          <stop offset="0" stop-color="#e8eef2"/>
          <stop offset="0.55" stop-color="#c9d2d8"/>
          <stop offset="0.8" stop-color="#d9452f"/>
          <stop offset="1" stop-color="#e36b2c"/>
        </linearGradient>
        <linearGradient id="swooshC" x1="0" x2="1">
          <stop offset="0" stop-color="#7cbf2c"/><stop offset="1" stop-color="#1f3f93"/>
        </linearGradient>
        <linearGradient id="swooshD" x1="0" x2="1">
          <stop offset="0" stop-color="#1f3f93"/><stop offset="1" stop-color="#7cbf2c"/>
        </linearGradient>
      </defs>
      <path role="img" aria-label="Photo of a chef slicing capsicum on a chopping board in a kitchen" d="M0 60C150 90 330 70 440 30V510C330 470 120 470 0 515Z" fill="url(#kitchenTones)"/>
      <path d="M0 20C140 60 330 50 440 5V15C330 60 140 70 0 40Z" fill="#1f3f93"/>
      <path d="M0 40C140 70 330 60 440 15V30C330 75 150 86 0 60Z" fill="url(#swooshC)"/>
      <path d="M0 515C120 470 330 470 440 510V525C330 485 120 488 0 535Z" fill="url(#swooshD)"/>
      <path d="M0 535C120 488 330 485 440 525V560C330 505 120 508 0 548Z" fill="#1f3f93"/>
    </svg>
    <div class="contact">
      <p class="contact__name">Daniel Whitford</p>
      <p class="contact__line">Call us : 0400 555 218</p>
      <p class="contact__line">Email us daniel.w.nutrition@example.com</p>
      <p class="contact__fax">Fax: 6300 4417</p>
      <p class="contact__web">www.riverbenddietitian.example</p>
      <p class="contact__role">Verified clinical mealwise &amp; Chef</p>
    </div>
    <div class="badge" role="img" aria-label="Certification badge"></div>
  </section>

</main>
</body>
</html>
```